Business card design and logo needed - Photographer

I take photos of weddings, rodeos, snowmobiling.
Need a card to hand out to prospective clients.
Industry/Entity Type
Business
Contact Information for Business Card
Marcus Dolven Photography
Requirements
Must have
- Bold
Black or white base.
My website. www.MarcusDolven.example
Should not have
- camera/ lens/ aperture blades

```html
<!DOCTYPE html>
<html lang="en">
<head>
<meta charset="utf-8">
<title>Marcus Dolven Photography — Business Card</title>
<link rel="stylesheet" href="https://fonts.googleapis.com/css2?family=Inter:wght@400;700&display=swap">
<style>
  :root {
    --card-bg: #141414;
    --name-ink: #ffffff;
    --muted-ink: #3d3c4a;
  }
  html, body {
    margin: 0;
    padding: 0;
    width: 1200px;
    height: 693px;
    overflow: hidden;
    background: var(--card-bg);
  }
  .card {
    position: relative;
    width: 1200px;
    height: 693px;
    background: var(--card-bg);
    font-family: "Helvetica Neue", Helvetica, Arial, "Inter", sans-serif;
  }
  .wordmark {
    position: absolute;
    left: 0;
    right: 0;
    top: 196px;
    text-align: center;
    margin: 0;
  }
  .wordmark__name {
    display: block;
    color: var(--name-ink);
    font-weight: 700;
    font-size: 115px;
    line-height: 1;
    letter-spacing: 0;
  }
  .wordmark__trade {
    display: block;
    color: var(--muted-ink);
    font-weight: 700;
    font-size: 112px;
    line-height: 1;
    margin-top: -14px;
    letter-spacing: 1px;
  }
  .website {
    position: absolute;
    left: 0;
    right: 0;
    top: 582px;
    text-align: center;
    margin: 0;
    color: var(--muted-ink);
    font-weight: 400;
    font-size: 47px;
    line-height: 1;
  }
</style>
</head>
<body>
  <main class="card">
    <h1 class="wordmark">
      <span class="wordmark__name">Marcus Dolven</span>
      <span class="wordmark__trade">Photography</span>
    </h1>
    <p class="website">www.MarcusDolven.example</p>
  </main>
</body>
</html>
```